Technology Solutions Provider

Let’s design a business card that will be as simple and bold at the same time. Name, email address, website & phone number.

Target Market(s)

Small to Medium Size Business

Industry/Entity Type

It Professional

Contact Information for Business Card

Name, email, website, phone numbers

Font styles to use
Sans Serif

Colors
ec1f27
f04a50
dddddd
919191
000000
ffffff

Requirements
Must have
• Clean simple look using my existing logo. I just need to the basic contact information on this card.
Nice to have
• Im considering the square size card versus the standard size business card.
Should not have
• No Mailing Address, no list of services.

```html
<!DOCTYPE html>
<html lang="en">
<head>
<meta charset="utf-8">
<title>Halden Systems – Business Card</title>
<link rel="stylesheet" href="https://fonts.googleapis.com/css2?family=Exo+2:wght@400;700&display=swap">
<style>
  :root {
    --red: #ec1f27;
    --red-soft: #f04a50;
    --stage: #dddddd;
    --grey: #919191;
    --black: #000000;
    --white: #ffffff;
    --paper: #f4f4f4;
  }
  * { margin: 0; padding: 0; box-sizing: border-box; }
  html, body {
    width: 1200px;
    height: 1000px;
    overflow: hidden;
    background: var(--stage);
    font-family: "Exo 2", Arial, sans-serif;
  }
  .card-set {
    position: absolute;
    top: 350px;
    left: 60px;
    display: flex;
    gap: 40px;
  }
  .card {
    position: relative;
    width: 520px;
    height: 300px;
    border-radius: 24px;
    overflow: hidden;
    box-shadow: 0 10px 24px rgba(0,0,0,0.18);
  }

  /* Front */
  .card-front {
    background: var(--paper);
  }
  .card-front .edge-band {
    position: absolute;
    left: 0; top: 0; bottom: 0;
    width: 52px;
    background: var(--black);
  }
  .brand {
    position: absolute;
    left: 52px; right: 0; top: 0; bottom: 0;
    display: flex;
    align-items: center;
    justify-content: center;
    gap: 12px;
  }
  .brand-dot {
    width: 14px;
    height: 14px;
    border-radius: 50%;
    background: var(--red);
  }
  .brand-name {
    font-size: 34px;
    font-weight: 400;
    color: var(--black);
    letter-spacing: 0.5px;
  }

  /* Back */
  .card-back {
    background: linear-gradient(135deg, var(--red) 0%, var(--red) 60%, #e52a30 100%);
  }
  .card-back .edge-band {
    position: absolute;
    left: 0; top: 0; bottom: 0;
    width: 68px;
    background: var(--paper);
  }
  .holder-name {
    position: absolute;
    left: 112px;
    top: 196px;
    font-size: 24px;
    font-weight: 700;
    color: var(--black);
  }
  .divider {
    position: absolute;
    left: 272px;
    top: 168px;
    width: 1.5px;
    height: 100px;
    background: var(--black);
  }
  .contact-list {
    position: absolute;
    left: 290px;
    top: 176px;
    list-style: none;
    font-size: 16px;
    line-height: 25px;
    color: var(--black);
  }
  .contact-web {
    font-weight: 700;
    font-size: 19px;
    color: var(--white);
  }
</style>
</head>
<body>
  <main class="card-set">
    <section class="card card-front" aria-label="Card front">
      <div class="edge-band"></div>
      <div class="brand">
        <span class="brand-dot"></span>
        <span class="brand-name">Halden Systems</span>
      </div>
    </section>

    <section class="card card-back" aria-label="Card back">
      <div class="edge-band"></div>
      <p class="holder-name">lorem ipsum</p>
      <div class="divider"></div>
      <ul class="contact-list">
        <li class="contact-phone">+22 33 44 5678</li>
        <li class="contact-web">yourwebsite.com</li>
        <li class="contact-email">your_email@domain.com</li>
      </ul>
    </section>
  </main>
</body>
</html>
```